Web Design Project

Brightwater Digital owns and operates a large number of editorial websites. These websites provides mostly consumers in the financial services space with information and price comparisons for a particular service.

Brightwater Digital, as the holding company for each of these sites, currently has no website. We need to build a website targeted towards potential partners for our websites. The idea being that when we start a conversation with a partner, they can view our site and obtain some basic information about who we are.

The structure of the site is to be very simple, containing only a brief description about who we are, our contact details and a list of some of our websites:
• CoverQuest.net.au
• AutoPolicyMatcher.com.au
• NestPolicyMatcher.com.au
• WellPolicyMatcher.com.au
• CoverQuestMatcher.com.au
• TripPolicyMatcher.com.au
• CritterPolicyMatcher.com.au
• CashAdvanceMatcher.com.au
• MobileCoolingUnit.com.au
• FixedSaverYields.com.au
• ThriftyHabits.com.au
• PurseGran.com.au
• TameThePlastic.com.au
• PurseMinder.com.au
• ThirdPartyClaimsCoverOzland.com.au
• Trade-Protect.com.au
• AutoPolicyProviders.com.au
• WellPolicyProviders.com.au
• NestPolicyOzland.com
• CoverQuestOzland.com
• WageShieldPolicyOzland.com
• WellPolicyOzland.com
• CritterPolicyOzland.com
• CashAdvancesOzland.com
• PlasticPaysOzland.com
• NestLendersOzland.com
• NestEggFunds.net.au

The design of the site should say 'Internet company', 'professional', 'fresh thinking'. The design should not look like a corporate site that you would see from any corporate services business with images of people in suits. We are ultimately an Internet business and there should be a unique feel to the site.

We are open to a suggestion of a colour pallet as the holding company does not have an established logo.

Some sites that we like are:

http://www.prismwork-studio.co.uk/#home
http://sample00.layoutvault.example/wt_48248/index.html
http://sample00.layoutvault.example/wordpress_46388/
http://mindvolt.example/
http://www.tandora.us/
http://www.kelvorabintu.example/
http://www.slickfrontpages.example/Corporate/design-ideas-detail.html?id=7916
http://trebla.example/
http://orvantek.example/

Reason: Hi all, Apologies, but I need to extend the timeline. One of our key stakeholders is away for the next week. There are a few good designs that we have received to date and there are some tweaks that we would like to see before making a final decision. Thank you to everyone that has submitted designs - Have a great new year. Derek

Reason: Sorry to have to delay the deadline on this, but we did not find anything in the designs really resonated with us. We will have a further think about the existing designs that have been submitted and how we can provide more specific feedback to the designers to make some modifications to the designs.

Target Market(s)

We are targeting insurance companies / brokers that we are talking to. The idea is that we show a professional face to them.

Industry/Entity Type

Financial

Requirements
Must have
• Home Page (possibly integrated with About us details)
Contact Us
Our Sites

```html
<!DOCTYPE html>
<html lang="en">
<head>
<meta charset="utf-8">
<title>Our Sites – Brightwater Digital</title>
<link rel="stylesheet" href="https://fonts.googleapis.com/css2?family=Anton&family=Open+Sans:wght@400;600;700&display=swap">
<style>
:root{
  --sky-top:#0a7fe8;
  --sky-bottom:#c4e2fb;
  --navy:#063a6b;
  --page-grey:#c8c8c8;
  --white:#ffffff;
  --blue:#1a8cff;
  --ink:#333333;
  --list-bg:#e8e8e8;
  --divider:#c9c9c9;
  --orange:#f7941d;
  --green:#3cb43c;
  --link-blue:#3a8ee6;
  --nav-link:#bcdcff;
  --gold:#f2a900;
  --card:#666666;
  --card-active:#333333;
  --card-border:#8a8a8a;
  --footer-top:#07263f;
  --footer-bottom:#000000;
}
*{margin:0;padding:0;box-sizing:border-box}
html,body{width:889px;height:1200px;overflow:hidden;background:var(--page-grey)}
body{font-family:"Open Sans",Verdana,sans-serif;color:var(--ink)}
.stage{width:1000px;height:1350px;position:relative;transform:scale(.889);transform-origin:0 0;
  background:linear-gradient(to bottom,var(--navy) 0,var(--navy) 14px,var(--sky-top) 14px,var(--sky-bottom) 200px,var(--page-grey) 200px)}
.brand{position:absolute;left:62px;top:24px;font-family:"Open Sans",sans-serif;font-weight:600;color:var(--white);font-size:24px;line-height:32px}
.nav{position:absolute;left:62px;top:69px;display:flex;gap:31px;font-size:14px}
.nav a{color:var(--nav-link);text-decoration:none}
.nav a.current{color:var(--white)}
.sheet{position:absolute;left:20px;top:145px;width:960px;height:1160px;background:var(--white);border-radius:16px 16px 0 0}
.page-title{position:absolute;left:41px;top:8px;font-family:"Anton",sans-serif;color:var(--blue);font-size:44px;font-weight:400;letter-spacing:.5px}
.section-title{position:absolute;left:41px;font-size:18.5px;font-weight:400;color:var(--ink)}
.directory{position:absolute;left:30px;top:126px;width:903px;height:276px;background:var(--list-bg);display:flex;padding-top:17px}
.dir-col{width:304px;padding-left:12px;border-left:1px solid var(--divider);height:234px;margin-top:4px}
.dir-col:first-child{border-left:none}
.dir-col h3{font-size:12.5px;font-weight:700;letter-spacing:.7px;text-transform:uppercase;margin:-4px 0 3px}
.dir-col h3.insurance{color:var(--orange)}
.dir-col h3.finance{color:var(--green)}
.dir-col h3.products{color:var(--link-blue);margin-top:15px}
.dir-col ul{list-style:none;font-size:12.8px;line-height:18px;letter-spacing:.3px}
.featured{position:absolute;left:30px;top:481px;width:903px;display:grid;grid-template-columns:repeat(3,295px);column-gap:9px;row-gap:20px}
.site-card{height:276px;background:var(--card);border:2px solid var(--card-border);color:var(--white)}
.site-card.active{background:var(--card-active)}
.card-mark{height:84px;display:flex;align-items:center;justify-content:center;gap:10px;font-size:26px;font-weight:600}
.card-mark.light{background:var(--white);color:#444}
.card-mark.dark{background:#000;color:var(--white);font-size:21px}
.card-mark.active{background:#2a2a2a;color:var(--gold)}
.dot{width:22px;height:22px;border-radius:50%;background:currentColor}
.square{width:16px;height:16px;background:currentColor}
.site-url{font-size:14px;margin:16px 0 0 7px}
.site-card.active .site-url{color:var(--gold)}
.site-desc{font-size:12.4px;line-height:14.5px;margin:11px 7px 0}
.footer{position:absolute;left:0;top:1293px;width:1000px;height:57px;background:linear-gradient(to bottom,var(--footer-top),var(--footer-bottom));
  color:var(--white);font-size:13px;padding:18px 0 0 61px}
</style>
</head>
<body>
<div class="stage">
  <div class="brand">Brightwater Digital</div>
  <nav class="nav"><a href="#">Home</a><a href="#" class="current">Our Sites</a><a href="#">Contact Us</a></nav>

  <main class="sheet">
    <h1 class="page-title">OUR SITES</h1>
    <h2 class="section-title" style="top:90px">Complete directory listing</h2>

    <section class="directory">
      <div class="dir-col">
        <h3 class="insurance">Insurance</h3>
        <ul>
          <li>Trade-Protect.com.au</li><li>AutoPolicyProviders.com.au</li><li>AutoPolicyMatcher.com.au</li>
          <li>WellPolicyOzland.com</li><li>WellPolicyProviders.com.au</li><li>WellPolicyMatcher.com.au</li>
          <li>NestPolicyOzland.com</li><li>NestPolicyMatcher.com.au</li><li>WageShieldPolicyOzland.com</li>
          <li>CoverQuest.net.au</li><li>CoverQuestOzland.com</li><li>CoverQuestMatcher.com.au</li>
        </ul>
      </div>
      <div class="dir-col">
        <h3 class="insurance">Insurance continued</h3>
        <ul>
          <li>CashAdvancesOzland.com</li><li>CashAdvanceMatcher.com.au</li><li>CritterPolicyOzland.com</li>
          <li>CritterPolicyMatcher.com.au</li><li>ThirdPartyClaimsCoverOzland.com.au</li><li>TripPolicyMatcher.com.au</li>
        </ul>
      </div>
      <div class="dir-col">
        <h3 class="finance">Money &amp; Finance</h3>
        <ul>
          <li>PlasticPaysOzland.com</li><li>ThriftyHabits.com.au</li><li>NestLendersOzland.com</li>
          <li>TameThePlastic.com.au</li><li>PurseGran.com.au</li><li>NestEggFunds.net.au</li>
          <li>FixedSaverYields.com.au</li><li>PurseMinder.com.au</li>
        </ul>
        <h3 class="products">Products</h3>
        <ul><li>MobileCoolingUnit.com.au</li></ul>
      </div>
    </section>

    <h2 class="section-title" style="top:445px">Featured sites</h2>

    <section class="featured">
      <article class="site-card">
        <div class="card-mark light"><span class="dot"></span>CoverQuest</div>
        <p class="site-url">www.coverquest.net.au</p>
        <p class="site-desc">Phasellus sagittis mi at massa bibendum feugiat. In sed nisl quam, vitae hendrerit magna. Nunc id mauris vel nisl sagittis venenatis ut eget velit. Nam fringilla sapien sed nunc fringilla ac mollis ante porta. Quisque ultricies viverra cursus. Phasellus non vehicula dui. Donec pretium pharetra nunc sit amet aliquam. Vestibulum vulputate imperdiet odio. Proin in mollis tellus.</p>
      </article>
      <article class="site-card active">
        <div class="card-mark active">ThriftyHabits</div>
        <p class="site-url">www.thriftyhabits.com.au</p>
        <p class="site-desc">Nam tellus elit, bibendum et vulputate vitae, scelerisque a enim. Pellentesque odio ligula, accumsan sed tempor luctus, auctor nec elit. Praesent sed scelerisque libero. Sed lorem neque, lacinia sit amet adipiscing sit amet, dapibus quis erat. Morbi vulputate mattis enim, eget viverra ipsum elementum eu.</p>
      </article>
      <article class="site-card">
        <div class="card-mark light"><span class="dot"></span>PurseGran</div>
        <p class="site-url">www.pursegran.com.au</p>
        <p class="site-desc">Cras a est neque. Pellentesque hendrerit, tellus sed porta porttitor, orci quam dictum nisl, id viverra eros leo at turpis. Fusce sagittis tincidunt mi ut convallis. Curabitur vel diam at ante convallis molestie ac in libero. Maecenas quis neque nec metus lobortis vulputate. Sed volutpat, enim ac viverra ultricies, velit eros imperdiet lectus, ac euismod leo erat at nisi.</p>
      </article>
      <article class="site-card">
        <div class="card-mark light">AutoPolicyMatcher</div>
        <p class="site-url">www.autopolicymatcher.com.au</p>
        <p class="site-desc">Class aptent taciti sociosqu ad litora torquent per conubia nostra, per inceptos himenaeos. Quisque ultricies, lorem quis sodales vehicula, velit tortor auctor velit, eget viverra odio nulla ut nisl. Morbi tincidunt leo sit amet massa dapibus vulputate. Aliquam vestibulum dictum bibendum. Pellentesque mauris lorem, vehicula a auctor eget, suscipit non urna.</p>
      </article>
      <article class="site-card">
        <div class="card-mark dark"><span class="square"></span>CritterPolicyMatcher</div>
        <p class="site-url">www.critterpolicymatcher.com.au</p>
        <p class="site-desc">Fusce quam massa, condimentum vitae ornare eget, rhoncus quis tortor. Proin id eros ut enim lobortis hendrerit. Aenean bibendum, nibh a fermentum cursus, purus erat ultricies enim, in bibendum arcu augue eget nibh. Pellentesque bibendum diam eget massa iaculis vel cursus felis feugiat. Cras ut nulla ipsum.</p>
      </article>
      <article class="site-card">
        <div class="card-mark dark"><span class="square"></span>TripPolicyMatcher</div>
        <p class="site-url">www.trippolicymatcher.com.au</p>
        <p class="site-desc">Nullam dapibus congue nulla, eu tristique tellus condimentum at. Nunc tellus elit, bibendum at euismod non, congue non urna. Cras nec nibh vitae felis ultricies fermentum. Nulla facilisi. Pellentesque sit amet sem libero, eu suscipit urna. Sed pharetra sagittis erat, nec sagittis tellus tristique eget. Proin tincidunt adipiscing ante, non vulputate tellus dapibus eget. Mauris in lectus urna, ac tempor sem.</p>
      </article>
    </section>
  </main>

  <footer class="footer">© 2012 Brightwater Digital</footer>
</div>
</body>
</html>
```